Brand new letterhead, business card, email signature etc.

We are a financial company in London, UK. Our website is www.quorvane.com. We're wanting a complete remodel of the company colours, letter head, business cards, email signatures, etc. Looking to keep the same font for the company name. I have upload a colour palette that we want to work with. We're looking for company letterhead for outgoing letters/ correspondence, letterhead for internal documentation, email signatures, e-letters. etc. Ultimately we will redesign the entire website also. It is important that our clients get a strong, secure, warm, trustworthy, solid feeling and first impression.
Updates

Designs look the same

Target Market(s)

Institutional investors, (ultra) high net worth individuals

Industry/Entity Type

Finance, Invesments banking.

Font styles to use
Other font styles liked:
• Current font is "Champagne & Limousines"

Requirements
Must have
• Must use the colours provided on the PDF uploaded to the portal. The purple = main colour. The red = accent colour.
Nice to have
• Nice to use same font as now for the company name "Marlowin". Font is "Champagne & Limousines". Nice to have some reference to the old logo flower, but only subtle.
Should not have
• Do not use the colour red from our website. Use the colours provided on the colour palette PDF that I uploaded in the portal.

```html
<!DOCTYPE html>
<html lang="en">
<head>
<meta charset="utf-8">
<title>Marlowin Letterhead</title>
<link href="https://fonts.googleapis.com/css2?family=Josefin+Sans:wght@300&family=Open+Sans:wght@400&display=swap" rel="stylesheet">
<style>
  :root {
    --backdrop: #e8e8e8;
    --paper: #ffffff;
    --accent-red: #d9381a;
    --main-purple: #2b0019;
    --ink: #2a2a2a;
    --watermark: #f1eeee;
  }
  * { margin: 0; padding: 0; box-sizing: border-box; }
  html, body { width: 1200px; height: 799px; overflow: hidden; background: var(--backdrop); }
  .canvas { position: relative; width: 1200px; height: 799px; }
  .letterhead {
    position: absolute; left: 332px; top: 20px;
    width: 535px; height: 760px;
    background: var(--paper);
    box-shadow: 0 2px 10px rgba(0,0,0,0.15);
    overflow: hidden;
  }
  .bar { position: absolute; }
  .bar--red-left { left: 0; top: 47px; width: 54px; height: 11px; background: var(--accent-red); }
  .bar--purple-left { left: 0; top: 66px; width: 54px; height: 25px; background: var(--main-purple); }
  .bar--red-right { left: 249px; top: 44px; width: 286px; height: 11px; background: var(--accent-red); }
  .bar--purple-right { left: 249px; top: 61px; width: 286px; height: 28px; background: var(--main-purple); }
  .brand { position: absolute; left: 61px; top: 47px; height: 44px; display: flex; align-items: center; gap: 9px; }
  .brand__mark { width: 44px; height: 44px; border: 1px solid var(--ink); flex: none; }
  .brand__name {
    font-family: "Josefin Sans", sans-serif; font-weight: 300;
    font-size: 20px; letter-spacing: 2px; color: var(--ink);
    text-transform: uppercase; padding-top: 5px; white-space: nowrap;
    max-width: 128px; overflow: hidden;
  }
  .watermark {
    position: absolute; left: 122px; top: 222px; width: 297px; height: 316px;
    background: radial-gradient(ellipse at center, var(--watermark) 0%, rgba(241,238,238,0) 70%);
  }
  .contacts {
    position: absolute; left: 54px; top: 688px;
    display: grid; grid-template-columns: 152px auto; row-gap: 5px;
    font-family: "Open Sans", sans-serif; font-size: 10px; color: var(--ink);
  }
  .contact { display: flex; align-items: center; gap: 6px; white-space: nowrap; }
  .contact svg { width: 12px; height: 12px; flex: none; }
  .corner { position: absolute; left: 0; top: 0; width: 535px; height: 760px; }
</style>
</head>
<body>
<div class="canvas">
  <div class="letterhead">
    <div class="bar bar--red-left"></div>
    <div class="bar bar--purple-left"></div>
    <div class="bar bar--red-right"></div>
    <div class="bar bar--purple-right"></div>
    <div class="brand">
      <div class="brand__mark"></div>
      <span class="brand__name">Marlowin</span>
    </div>
    <div class="watermark" role="img" aria-label="Faint brand flower watermark"></div>
    <div class="contacts">
      <div class="contact">
        <svg viewBox="0 0 12 12"><circle cx="6" cy="6" r="5.3" fill="none" stroke="#d9381a" stroke-width="1"/><path d="M4 3.5l1 1-0.6 0.8q0.8 1.6 2.3 2.3l0.8-0.6 1 1-0.8 0.9q-2.8-0.6-4.6-4.6z" fill="#d9381a"/></svg>
        <span>+44 20 7946 0321</span>
      </div>
      <div class="contact">
        <svg viewBox="0 0 12 12"><path d="M6 1.2a3.4 3.4 0 0 1 3.4 3.4C9.4 7 6 10.8 6 10.8S2.6 7 2.6 4.6A3.4 3.4 0 0 1 6 1.2z" fill="none" stroke="#d9381a" stroke-width="1"/><circle cx="6" cy="4.6" r="1.3" fill="#d9381a"/></svg>
        <span>12 Aldermary Lane, London</span>
      </div>
      <div class="contact">
        <svg viewBox="0 0 12 12"><circle cx="6" cy="6" r="5.3" fill="none" stroke="#d9381a" stroke-width="1"/><rect x="3" y="4" width="6" height="4.2" fill="#d9381a"/><path d="M3 4l3 2.3L9 4" fill="none" stroke="#fff" stroke-width="0.7"/></svg>
        <span>hello@quorvane.com</span>
      </div>
      <div class="contact">
        <svg viewBox="0 0 12 12"><circle cx="6" cy="6" r="5.3" fill="none" stroke="#d9381a" stroke-width="1"/><circle cx="6" cy="6" r="3.4" fill="none" stroke="#d9381a" stroke-width="0.6"/><path d="M2.6 6h6.8M6 2.6q-1.8 3.4 0 6.8M6 2.6q1.8 3.4 0 6.8" fill="none" stroke="#d9381a" stroke-width="0.6"/></svg>
        <span>www.quorvane.com</span>
      </div>
    </div>
    <svg class="corner" viewBox="0 0 535 760" aria-hidden="true">
      <polygon points="0,740 432,736 412,760 0,760" fill="var(--main-purple)"/>
      <polygon points="412,760 535,760 535,660" fill="var(--accent-red)"/>
      <polyline points="535,619 443,716 487,760" fill="none" stroke="var(--main-purple)" stroke-width="2.5"/>
    </svg>
  </div>
</div>
</body>
</html>
```